Fall Event Advertisement for Porchlight Magazine

I will be taking out an ad in Porchlight Magazine to promote the fall events in our community. The audience is middle to upper class, primarily women, looking for fun activities and weekend getaways. The add should include our logo, contact info, a heading, like Discover Brindlewood County Fall Festivals & Events or something like that. I appreciate the creativity with the copy.

I have uploaded some photos. They all do not need to be used.

Contact info: Brindlewood Chamber of Commerce & Tourism
418 N Quarry Ln
Harlow Falls, NC 28000
(555) 318-2096
For a full listing of year-round events, check out our calendar here, www.thebrindlewoodchamber.example

Ad size: 8.25 inches x 10.875 inches

```html
<!DOCTYPE html>
<html lang="en">
<head>
<meta charset="utf-8">
<title>Discover Brindlewood County – Fall Festivals &amp; Events</title>
<link href="https://fonts.googleapis.com/css2?family=Bebas+Neue&family=Lobster&family=Montserrat:wght@500;600;700&display=swap" rel="stylesheet">
<style>
  :root {
    --wood-dark: #3b2a20;
    --wood-mid: #5a4132;
    --leaf-orange: #d9692b;
    --leaf-amber: #c98a3a;
    --accent-orange: #e0743a;
    --accent-green: #2f8f1f;
    --brush-green: #2a9a1c;
    --text-white: #ffffff;
    --paper: #ffffff;
    --navy: #26348a;
    --ink-grey: #555555;
    --page-bg: #d9d3cc;
  }
  * { margin: 0; padding: 0; box-sizing: border-box; }
  html, body { width: 758px; height: 1200px; overflow: hidden; background: var(--page-bg); }
  .ad {
    position: relative;
    width: 758px; height: 1200px;
    overflow: hidden;
    background: var(--paper);
    font-family: "Montserrat", Arial, sans-serif;
  }
  .wood {
    position: absolute; inset: 0;
    background:
      repeating-linear-gradient(90deg, rgba(0,0,0,0) 0 118px, rgba(0,0,0,.18) 118px 121px),
      linear-gradient(180deg, var(--wood-mid), var(--wood-dark) 55%, var(--wood-mid));
  }
  .leaf-border {
    position: absolute; inset: 0;
    background:
      radial-gradient(circle at 8% 6%, rgba(217,105,43,.7) 0 40px, rgba(217,105,43,0) 85px),
      radial-gradient(circle at 38% 2%, rgba(201,138,58,.6) 0 30px, rgba(201,138,58,0) 70px),
      radial-gradient(circle at 92% 5%, rgba(217,105,43,.7) 0 45px, rgba(217,105,43,0) 90px),
      radial-gradient(circle at 2% 35%, rgba(201,138,58,.6) 0 30px, rgba(201,138,58,0) 75px),
      radial-gradient(circle at 98% 30%, rgba(217,105,43,.6) 0 30px, rgba(217,105,43,0) 75px),
      radial-gradient(circle at 6% 70%, rgba(201,138,58,.55) 0 35px, rgba(201,138,58,0) 80px),
      radial-gradient(circle at 95% 68%, rgba(201,138,58,.55) 0 35px, rgba(201,138,58,0) 80px);
  }
  .bottom-panel { position: absolute; left: 0; top: 900px; width: 758px; height: 300px; }

  .headline { position: absolute; left: 0; width: 758px; text-align: center; color: var(--text-white); }
  .headline__discover {
    top: 52px;
    font-family: "Bebas Neue", Impact, sans-serif;
    font-size: 146px; line-height: 1; letter-spacing: -1px;
  }
  .headline__rule { position: absolute; left: 200px; width: 365px; height: 2px; background: var(--text-white); }
  .headline__rule--top { top: 184px; }
  .headline__rule--bottom { top: 232px; }
  .headline__county {
    top: 190px;
    font-weight: 600; font-size: 34px; letter-spacing: 1px;
    color: var(--accent-orange); line-height: 40px;
  }
  .headline__script {
    top: 238px;
    font-family: "Lobster", cursive; font-size: 40px; line-height: 46px;
  }

  .section-banner { position: absolute; left: 200px; top: 320px; width: 360px; height: 66px; }
  .section-banner__label {
    position: absolute; inset: 0;
    display: flex; align-items: center; justify-content: center;
    color: var(--text-white); font-weight: 600; font-size: 28px;
  }

  .event { position: absolute; text-align: center; font-size: 12px; line-height: 16px; color: var(--text-white); }
  .event__name { color: var(--accent-orange); font-weight: 600; font-size: 14px; }
  .event__date { font-weight: 700; font-size: 14px; }
  .event__place { color: var(--accent-green); font-weight: 600; font-size: 14px; }
  .event--center { left: 229px; width: 300px; }

  .photo {
    position: absolute; background: var(--paper); padding: 10px 10px 26px;
    box-shadow: 0 4px 10px rgba(0,0,0,.45);
  }
  .photo__image { width: 100%; height: 100%; }
  .photo--parade { left: -10px; top: 304px; width: 212px; height: 190px; transform: rotate(-5deg); }
  .photo--dancer { left: -10px; top: 504px; width: 222px; height: 226px; transform: rotate(3deg); }
  .photo--trumpet { left: 588px; top: 236px; width: 190px; height: 252px; transform: rotate(4deg); }
  .photo--food { left: 552px; top: 490px; width: 220px; height: 236px; transform: rotate(-4deg); }
  .photo--parade .photo__image { background: linear-gradient(160deg, #7fb05a, #3c5a8c 60%, #b23a3a); }
  .photo--dancer .photo__image { background: linear-gradient(160deg, #8a9a5c, #b7492e 50%, #3e5a2c); }
  .photo--trumpet .photo__image { background: linear-gradient(160deg, #6fa0dc, #2e3f9a 60%, #1a2458); }
  .photo--food .photo__image { background: linear-gradient(180deg, #6e8fb8, #3a2f2a 45%, #c9a259); }

  .chamber { position: absolute; left: 56px; top: 1090px; display: flex; align-items: center; gap: 10px; }
  .chamber__mark { width: 34px; height: 34px; border-radius: 50%; background: var(--accent-orange); }
  .chamber__name { color: var(--navy); font-weight: 700; font-size: 15px; line-height: 18px; }

  .calendar { position: absolute; left: 474px; top: 1028px; width: 284px; }
  .calendar__intro { color: var(--accent-green); font-weight: 700; font-size: 12px; line-height: 14px; padding-left: 8px; }
  .calendar__cta { color: var(--accent-orange); font-weight: 700; font-size: 12px; line-height: 14px; padding-left: 8px; }
  .calendar__url {
    margin-top: 4px; background: var(--accent-orange); color: var(--text-white);
    font-weight: 700; font-size: 13px; line-height: 22px; padding-left: 10px;
  }
  .contact { position: absolute; top: 1108px; display: flex; gap: 6px; color: var(--ink-grey); font-weight: 600; font-size: 14px; line-height: 15px; }
  .contact--phone { left: 400px; }
  .contact--address { left: 536px; }
  .contact__icon { width: 12px; height: 14px; flex: none; margin-top: 1px; }
</style>
</head>
<body>
<main class="ad">
  <div class="wood" role="img" aria-label="Dark brown wood plank texture"></div>
  <div class="leaf-border" role="img" aria-label="Border of orange autumn maple leaves"></div>

  <h1>
    <span class="headline headline__discover">DISCOVER</span>
    <span class="headline__rule headline__rule--top"></span>
    <span class="headline headline__county">BRINDLEWOOD COUNTY</span>
    <span class="headline__rule headline__rule--bottom"></span>
    <span class="headline headline__script">Fall Festivals &amp; Events</span>
  </h1>

  <div class="photo photo--parade"><div class="photo__image" role="img" aria-label="Photo of a hometown parade float with flags"></div></div>
  <div class="photo photo--dancer"><div class="photo__image" role="img" aria-label="Photo of a dancer in feathered regalia at a pow wow"></div></div>
  <div class="photo photo--trumpet"><div class="photo__image" role="img" aria-label="Photo of a marching band trumpet player"></div></div>
  <div class="photo photo--food"><div class="photo__image" role="img" aria-label="Photo of a festival food stand"></div></div>

  <div class="section-banner">
    <svg width="360" height="66" viewBox="0 0 360 70" preserveAspectRatio="none" aria-hidden="true">
      <path d="M22 12 L350 6 L336 22 L358 30 L340 44 L352 58 L24 64 L36 52 L4 46 L26 34 L2 24 Z" fill="var(--brush-green)"/>
    </svg>
    <h2 class="section-banner__label">Festivals &amp; Events</h2>
  </div>

  <div class="event event--center" style="top:420px">
    <div class="event__name">LAKESIDE LOOP,</div>
    <div class="event__date">SEPT 8-10</div>
    <div class="event__place">LAKE MERRITON, NC</div>
    <div>Run – Bike – Swim – Paddle</div>
  </div>
  <div class="event event--center" style="top:520px">
    <div class="event__name">HEARTHSIDE STEW FESTIVAL</div>
    <div class="event__date">SEPT 30</div>
    <div class="event__place">COBBLE CREEK, NC</div>
    <div>Parade – Family Fun – Good Eats</div>
  </div>
  <div class="event event--center" style="top:618px">
    <div class="event__name">BRINDLEWOOD COUNTY<br>AGRICULTURAL FAIR</div>
    <div class="event__date">OCT 4-9</div>
    <div class="event__place">HARLOW FALLS, NC</div>
    <div>Carnival Rides – Tractor Pull<br>Demolition Derby<br>Live Entertainment</div>
  </div>
  <div class="event" style="left:96px;width:330px;top:768px">
    <div class="event__name">RIVERBEND HERITAGE POW WOW</div>
    <div class="event__date">OCT 20-21</div>
    <div class="event__place">ASHGROVE, NC</div>
    <div>Traditional Foods - History<br>American Indian Dance &amp; Drumming Competition</div>
  </div>
  <div class="event" style="left:425px;width:180px;top:768px">
    <div class="event__name">GOLDEN YAM FESTIVAL</div>
    <div class="event__date">OCT 28</div>
    <div class="event__place">FERNHILL, NC</div>
    <div>Arts &amp; Crafts – Parade<br>Food - Entertainment</div>
  </div>
  <div class="event event--center" style="top:880px">
    <div class="event__name">ORCHARD PECAN HARVEST FESTIVAL</div>
    <div class="event__date">NOV 10-11</div>
    <div class="event__place">HARLOW FALLS, NC</div>
    <div>Car Show – Entertainment<br>Burger Brawl – Beer Garden</div>
  </div>

  <svg class="bottom-panel" viewBox="0 900 758 300" aria-hidden="true">
    <path d="M0 922 Q330 1060 758 970 L758 1200 L0 1200 Z" fill="var(--paper)"/>
  </svg>

  <div class="chamber">
    <span class="chamber__mark"></span>
    <span class="chamber__name">Brindlewood Chamber<br>of Commerce &amp; Tourism</span>
  </div>

  <div class="calendar">
    <p class="calendar__intro">For a full listing of year-round events,</p>
    <p class="calendar__cta">CHECK OUT OUR CALENDAR HERE.</p>
    <p class="calendar__url">www.thebrindlewoodchamber.example</p>
  </div>

  <div class="contact contact--phone">
    <svg class="contact__icon" viewBox="0 0 12 14" aria-hidden="true"><path d="M2 1 L5 1 L6 4 L4 5.5 Q5.5 8.5 8 10 L9.5 8 L12 9.5 L11.5 12.5 Q5 13 1 3 Z" fill="var(--accent-orange)"/></svg>
    <span>(555) 318-2096</span>
  </div>
  <div class="contact contact--address">
    <svg class="contact__icon" viewBox="0 0 12 14" aria-hidden="true"><path d="M6 0 A5 5 0 0 1 11 5 C11 8.5 6 14 6 14 C6 14 1 8.5 1 5 A5 5 0 0 1 6 0 Z M6 3 A2 2 0 1 0 6 7 A2 2 0 1 0 6 3 Z" fill="var(--accent-orange)" fill-rule="evenodd"/></svg>
    <span>418 N Quarry Ln<br>Harlow Falls, NC 28000</span>
  </div>
</main>
</body>
</html>
```